business card for Franco-Turkish restaurant

We are a Franco-Turkish restaurant, Le Coquelicot, based in the Cotes d'Armor in Brittany, near the Pink Granite Coast. We serve mainly Turkish cuisine. We would like a card reminding Britain and Turkey. No flag. Color: turquoise (sea ..), green, red. There should be a space for 3 lines: name, address, phone / email

Industry/Entity Type

Fast Food Restaurant

Contact Information for Business Card

Dervan Oruzel
Addresse: 14 Rue Paul-Henri Dauvel, 22410 Kervalou, France
Tel:+33 2 96 47 83 09

Colors
33a6d7
f04a50
acd036

Nice to have
• Symbols of Britain and Turkey
Should not have
• No flags

```html
<!DOCTYPE html>
<html lang="fr">
<head>
<meta charset="utf-8">
<title>Le Coquelicot – carte de visite</title>
<link rel="stylesheet" href="https://fonts.googleapis.com/css2?family=Comfortaa:wght@700&family=Roboto+Condensed:wght@400&family=Roboto:wght@400&display=swap">
<style>
  :root {
    --cream: #fbecdd;
    --peach-light: #f9dcc7;
    --peach-mid: #fbc3a8;
    --coral-red: #f4826f;
    --leaf-green: #d9ebb4;
    --teal-light: #84d1d5;
    --teal: #14b9bd;
    --brand-teal: #1ab4b8;
    --tagline: #f0806a;
    --contact-ink: #0f6466;
  }
  * { margin: 0; padding: 0; box-sizing: border-box; }
  html, body {
    width: 1200px;
    height: 818px;
    overflow: hidden;
    background: var(--cream);
  }
  .card {
    position: relative;
    width: 1200px;
    height: 818px;
    overflow: hidden;
    background: var(--cream);
  }
  .card__waves {
    position: absolute;
    inset: 0;
    width: 1200px;
    height: 818px;
  }
  .wave--peach-light { fill: var(--peach-light); }
  .wave--peach-mid { fill: var(--peach-mid); }
  .wave--coral { fill: var(--coral-red); }
  .wave--green { fill: var(--leaf-green); }
  .wave--teal-light { fill: var(--teal-light); }
  .wave--teal { fill: var(--teal); }

  .brand {
    position: absolute;
    right: 170px;
    top: 130px;
    text-align: right;
  }
  .brand__name {
    font-family: "Comfortaa", sans-serif;
    font-weight: 700;
    font-size: 124px;
    line-height: 1;
    letter-spacing: -3px;
    color: var(--brand-teal);
  }
  .brand__tagline {
    font-family: "Roboto Condensed", sans-serif;
    color: var(--tagline);
    line-height: 1;
  }
  .brand__tagline--main {
    margin-top: 28px;
    font-size: 54px;
  }
  .brand__tagline--sub {
    margin-top: 8px;
    font-size: 38px;
  }

  .contact {
    position: absolute;
    left: 66px;
    top: 536px;
    list-style: none;
    font-family: "Roboto", sans-serif;
    font-size: 38px;
    color: var(--contact-ink);
  }
  .contact__item {
    display: flex;
    align-items: center;
    height: 52px;
    margin-bottom: 24px;
    white-space: nowrap;
  }
  .contact__icon {
    width: 44px;
    height: 44px;
    margin-right: 26px;
    fill: var(--contact-ink);
    flex: none;
  }
</style>
</head>
<body>
  <main class="card">
    <svg class="card__waves" viewBox="0 0 1200 818" aria-hidden="true">
      <path class="wave--peach-light" d="M520 0 H1200 V700 C1140 640 1100 560 1080 460 C1050 250 900 60 520 0 Z"/>
      <path class="wave--peach-mid" d="M640 0 H1200 V660 C1160 600 1140 520 1125 430 C1100 250 980 70 640 0 Z"/>
      <path class="wave--coral" d="M780 0 H1200 V620 C1180 560 1175 470 1165 390 C1145 230 1050 70 780 0 Z"/>
      <path class="wave--green" d="M0 330 C180 290 400 330 620 410 C850 495 1050 510 1200 480 V818 H0 Z"/>
      <path class="wave--teal-light" d="M0 410 C220 370 440 400 660 470 C880 540 1060 570 1200 560 V818 H0 Z"/>
      <path class="wave--teal" d="M0 475 C230 445 460 465 700 510 C900 550 1080 620 1200 635 V818 H0 Z"/>
    </svg>

    <header class="brand">
      <h1 class="brand__name">le coquelicot</h1>
      <p class="brand__tagline brand__tagline--main">restaurant</p>
      <p class="brand__tagline brand__tagline--sub">franco-turque</p>
    </header>

    <ul class="contact">
      <li class="contact__item">
        <svg class="contact__icon" viewBox="0 0 24 24" aria-hidden="true">
          <path d="M12 2a7 7 0 0 0-7 7c0 5.2 7 13 7 13s7-7.8 7-13a7 7 0 0 0-7-7zm0 9.6A2.6 2.6 0 1 1 12 6.4a2.6 2.6 0 0 1 0 5.2z"/>
        </svg>
        <span>14 Rue Paul-Henri Dauvel, 22410 Kervalou</span>
      </li>
      <li class="contact__item">
        <svg class="contact__icon" viewBox="0 0 24 24" aria-hidden="true">
          <path d="M12 1.5a10.5 10.5 0 1 0 0 21 10.5 10.5 0 0 0 0-21zm0 2a8.5 8.5 0 1 1 0 17 8.5 8.5 0 0 1 0-17z"/>
          <path d="M8.6 6.5l1.6-.4 1.1 2.6-1 .9c.6 1.3 1.6 2.4 2.9 3l.9-1 2.6 1.1-.4 1.6c-.2.7-.9 1.1-1.6 1-3.6-.6-6.4-3.4-7-7-.1-.7.3-1.4.9-1.8z"/>
        </svg>
        <span>+33 2 96 47 83 09</span>
      </li>
      <li class="contact__item">
        <svg class="contact__icon" viewBox="0 0 24 24" aria-hidden="true">
          <path d="M2 5h20v1.2L12 13.6 2 6.2z"/>
          <path d="M2 7.8l6.4 4.8L2 17.6z M22 7.8l-6.4 4.8 6.4 5z M9.6 13.5 12 15.3l2.4-1.8L21 19H3z"/>
        </svg>
        <span>bonjour@lecoquelicot-resto.fr</span>
      </li>
    </ul>
  </main>
</body>
</html>
```